REDESIGN COUPLE PAGES FOR VIMLO VIDEO ADS

PLEASE REDESIGN THIS PAGE FOR ME:
http://pageframequarry.com/kq/rudy/vimlo/pricing.html
I need it to be easy to read for the end user so the customer knows exactly what he will be getting. Make an emphasis on the subscription as the most popular item....and also the price per video format should be emphasized too.

Target Market(s)

B2B

Industry/Entity Type

Video Production

Number of Pages Required

3 page

Colors

Designer to choose colors to be used in the design.

Requirements
Must have
• PLEASE REDESIGN THIS PAGE FOR ME:
• http://pageframequarry.com/kq/rudy/vimlo/pricing.html
• I need it to be easy to read for the end user so the customer knows exactly what he will be getting. Make an emphasis on the subscription as the most popular item....and also the price per video format should be emphasized too.
Nice to have
Should not have

```html
<!DOCTYPE html>
<html lang="en">
<head>
<meta charset="utf-8">
<title>VIMLO – Checkout</title>
<link href="https://fonts.googleapis.com/css2?family=Source+Sans+3:wght@400;600;700&family=Oswald:wght@500&display=swap" rel="stylesheet">
<style>
:root{
  --navy:#141c2b;
  --page:#f8f9fb;
  --card:#ffffff;
  --line:#e6eaf0;
  --field:#f7f9fb;
  --field-line:#e1e6ec;
  --ink:#2b2f36;
  --muted:#6c7078;
  --pink-a:#ec88c2;
  --pink-b:#d96aa7;
  --blue-a:#66a6ee;
  --blue-b:#4f8de2;
  --red:#e0344a;
  --link:#3b8de0;
}
*{box-sizing:border-box;margin:0;padding:0}
html,body{width:1200px;height:1192px;overflow:hidden}
body{position:relative;background:var(--page);font-family:"Source Sans 3",sans-serif;color:var(--ink)}

.topbar{position:absolute;left:0;top:0;width:1200px;height:49px;background:var(--navy);color:#fff}
.brand{position:absolute;left:172px;top:10px;line-height:1}
.brand-name{font-size:19px;font-weight:700;letter-spacing:3px;color:#fff;display:flex;align-items:center;gap:6px}
.brand-name i{display:block;width:10px;height:10px;background:#4fb3ec}
.brand-tag{font-size:5.5px;font-weight:600;letter-spacing:.6px;color:#e8ecf2;margin-top:3px}
.nav{position:absolute;top:18px;left:434px;display:flex;gap:15px;font-size:10px}
.nav a{color:#fff;text-decoration:none}
.nav a.active{color:#4fa0e8}
.login{position:absolute;left:937px;top:19px;font-size:9.5px}
.signup{position:absolute;left:976px;top:12.5px;width:52px;height:24px;background:#3b87e6;border:1px solid #6aa8f0;font-size:9.5px;line-height:22px;text-align:center}

.page-title{position:absolute;top:82px;width:1200px;text-align:center;font-size:24px;font-weight:600;letter-spacing:.5px}
.page-sub{position:absolute;top:112px;width:1200px;text-align:center;font-size:10px;color:var(--muted)}

.form-card{position:absolute;left:253px;top:155px;width:456px;height:771px;background:var(--card);border:1px solid var(--line);border-radius:3px}
.h-section{position:absolute;font-size:15px;font-weight:600}
.h-sub{position:absolute;font-size:9px;color:var(--muted)}
.rule{position:absolute;left:12.5px;width:431px;height:1px;background:var(--line)}
.label{position:absolute;font-size:9px;color:var(--muted)}
.field{position:absolute;height:31px;background:var(--field);border:1px solid var(--field-line)}
.field svg{position:absolute;right:9px;top:9px}
.col-a{left:19px;width:203px}
.col-b{left:234px;width:203px}
.terms-title{position:absolute;left:19px;top:285px;font-size:11px;font-weight:600}
.terms-box{position:absolute;left:19px;top:306px;width:418px;height:93px;background:var(--field);border:1px solid var(--field-line);padding:12px 26px 0 16px;font-size:9px;line-height:15px;color:var(--muted)}
.scroll{position:absolute;right:0;top:0;width:9px;height:91px;border-left:1px solid var(--field-line);background:#fafafa}
.scroll i{position:absolute;left:1px;top:11px;width:7px;height:21px;background:#dcdcdc;border:1px solid #bbb}
.check{position:absolute;left:19px;top:413px;font-size:9px;color:var(--muted);display:flex;align-items:center;gap:6px}
.check span{width:7px;height:7px;border:1px solid #999;background:#f2f2f2}
.btn{position:absolute;top:718px;height:35px;color:#fff;font-size:11.5px;font-weight:600;text-align:center;line-height:35px;border-radius:2px}
.btn-order{left:19px;width:203px;background:linear-gradient(90deg,var(--pink-a),var(--pink-b))}
.btn-back{left:234px;width:203px;background:linear-gradient(90deg,var(--blue-a),var(--blue-b))}

.plan-card{position:absolute;left:728px;top:155px;width:219px;height:652px;background:var(--card);border:1px solid var(--line);border-radius:3px}
.plan-head{position:absolute;left:0;top:0;width:219px;height:74px;background:linear-gradient(90deg,var(--pink-a),var(--pink-b));border-radius:3px 3px 0 0;overflow:hidden;color:#fff}
.plan-name{position:absolute;left:20px;top:20px;font-size:15px;font-weight:600}
.plan-sub{position:absolute;left:20px;top:41px;font-size:9.5px}
.plan-head svg{position:absolute;left:173px;top:11px}
.notch{position:absolute;left:103px;top:73px;width:0;height:0;border-left:6px solid transparent;border-right:6px solid transparent;border-top:6px solid var(--pink-b)}
.from{position:absolute;left:19px;top:114px;font-size:9.5px;letter-spacing:.5px;color:var(--muted)}
.price{position:absolute;right:19px;top:98px;font-family:"Oswald",sans-serif;font-size:21px;color:var(--red);font-weight:500}
.price sup{font-size:10px;vertical-align:9px}
.price-unit{position:absolute;right:19px;top:125px;font-size:9.5px;color:var(--muted)}
.rule-s{position:absolute;left:12.5px;width:194px;height:1px;background:var(--line)}
.acc{position:absolute;left:19px;width:181px;font-size:9.5px;font-weight:600;letter-spacing:.6px;display:flex;justify-content:space-between;align-items:center}
.features{position:absolute;left:19px;top:205px;list-style:none;font-size:9px;color:var(--muted)}
.features li{height:18.1px;display:flex;align-items:center;gap:7px}
.features svg{flex:none}
.fscroll{position:absolute;left:196px;top:201px;width:2px;height:61px;background:#dfe7f1;border-radius:1px}
.qty-label{position:absolute;left:0;width:132px;top:470px;text-align:right;font-size:9px;color:var(--muted)}
.stepper{position:absolute;left:137.5px;top:465px;display:flex;align-items:center}
.stepper .pm{width:21px;height:21px;border-radius:50%;background:#e4ebf4;font-size:10px;text-align:center;line-height:20px;color:#7a8796}
.stepper .num{width:21px;height:21px;border-radius:50%;background:#fff;border:1px solid var(--field-line);font-size:7.5px;text-align:center;line-height:19px;margin:0 -1px;position:relative}
.sum-row{position:absolute;left:0;width:219px;font-size:9px}
.sum-row .k{position:absolute;right:93px;text-align:right;white-space:nowrap}
.sum-row .v{position:absolute;right:31px}
.sum-big{font-size:12px}
.sum-row.promo{color:var(--link)}
.red{color:var(--red)}

.footer{position:absolute;left:0;top:977px;width:1200px;height:215px;background:var(--navy);color:#fff}
.f-brand{position:absolute;left:253px;top:53px;font-size:30px;font-weight:700;letter-spacing:6px;display:flex;align-items:center;gap:10px;line-height:1}
.f-brand i{display:block;width:16px;height:16px;background:#4fb3ec}
.f-tag{position:absolute;left:253px;top:84px;font-size:10px;letter-spacing:1.2px;color:#e8ecf2}
.f-claim{position:absolute;left:253px;top:105px;font-size:12px;font-weight:700;letter-spacing:-.2px}
.f-head{position:absolute;top:53px;font-size:11.5px;font-weight:400}
.f-bar{position:absolute;top:73px;width:16px;height:1px;background:#55606f}
.f-links{position:absolute;left:550px;top:91px;list-style:none;font-size:9px}
.f-links li{height:20.6px}
.f-about{position:absolute;left:728px;top:90px;width:230px;font-size:10px;line-height:15.6px}
.socials{position:absolute;left:728px;top:151px;display:flex;gap:7px}
.socials span{width:24px;height:24px;border-radius:50%;background:#222d40;display:block}
</style>
</head>
<body>

<header class="topbar">
  <div class="brand">
    <div class="brand-name"><i></i>VIMLO</div>
    <div class="brand-tag">MARKETING VIDEOS MADE FOR YOU</div>
  </div>
  <nav class="nav">
    <a>Home</a><a>How It Works</a><a>Examples</a><a>FAQ</a><a>Contact Us</a><a class="active">Pricing</a><a>Calendar</a>
  </nav>
  <div class="login">Log In</div>
  <div class="signup">Sign Up</div>
</header>

<h1 class="page-title">CHECKOUT</h1>
<p class="page-sub">Fill out the form below to make your purchase</p>

<section class="form-card">
  <h2 class="h-section" style="left:17.5px;top:20px">Account Information</h2>
  <p class="h-sub" style="left:17.5px;top:41px">Create your account below</p>
  <div class="rule" style="top:74px"></div>

  <span class="label" style="left:19px;top:93px">First Name</span>
  <span class="label" style="left:234px;top:93px">Last Name</span>
  <div class="field col-a" style="top:112.5px"></div>
  <div class="field col-b" style="top:112.5px"></div>

  <span class="label" style="left:19px;top:156px">Email</span>
  <span class="label" style="left:234px;top:156px">Phone</span>
  <div class="field col-a" style="top:175px"></div>
  <div class="field col-b" style="top:175px"></div>

  <span class="label" style="left:19px;top:218px">Password</span>
  <span class="label" style="left:234px;top:218px">Confirm Password</span>
  <div class="field col-a" style="top:237.5px"></div>
  <div class="field col-b" style="top:237.5px"></div>

  <h3 class="terms-title">Terms &amp; Conditions</h3>
  <div class="terms-box">
    Lorem ipsum dolor sit amet, consectetur adipiscing elit, sed do eiusmod tempor incididunt ut labore et dolore magna aliqua. Ut enim ad minim veniam, quis nostrud exercitation ullamco laboris nisi ut aliquip ex ea commodo consequat. Duis aute irure dolor in reprehenderit in voluptate velit esse cillum dolore eu fugiat nulla pariatur.
    <div class="scroll"><i></i></div>
  </div>
  <label class="check"><span></span>I have read and accept the Terms &amp; Conditions.</label>

  <h2 class="h-section" style="left:19px;top:451px">Payment Details</h2>
  <p class="h-sub" style="left:19px;top:471px">Please enter your credit card details below.</p>
  <div class="rule" style="top:505px"></div>

  <span class="label" style="left:19px;top:524px">Cardholder Name</span>
  <span class="label" style="left:234px;top:524px">Email</span>
  <div class="field col-a" style="top:543px"></div>
  <div class="field col-b" style="top:543px"></div>

  <span class="label" style="left:19px;top:586px">Address Line 1</span>
  <span class="label" style="left:234px;top:586px">Zip Code</span>
  <div class="field col-a" style="top:605.5px"></div>
  <div class="field col-b" style="top:605.5px">
    <svg width="10" height="10" viewBox="0 0 10 10" style="top:10px"><path d="M3 4l2 2 2-2" fill="none" stroke="#777" stroke-width="1"/></svg>
  </div>

  <span class="label" style="left:19px;top:649px">Card Number</span>
  <span class="label" style="left:234px;top:649px">Expiration Date</span>
  <span class="label" style="left:356px;top:649px">CVV#</span>
  <div class="field col-a" style="top:668px"></div>
  <div class="field" style="left:234px;width:109px;top:668px">
    <svg width="11" height="11" viewBox="0 0 11 11"><rect x="1.5" y="2" width="8" height="7.5" fill="none" stroke="#aaa"/><path d="M1.5 4.5h8M3.5 1v2M7.5 1v2" stroke="#aaa"/></svg>
  </div>
  <div class="field" style="left:356px;width:81px;top:668px">
    <svg width="11" height="11" viewBox="0 0 11 11"><rect x="1" y="2.5" width="9" height="6.5" fill="none" stroke="#999"/><path d="M1 4.5h9" stroke="#999" stroke-width="1.2"/></svg>
  </div>

  <div class="btn btn-order">Place Your Order</div>
  <div class="btn btn-back">Back to Pricing Packages</div>
</section>

<aside class="plan-card">
  <div class="plan-head">
    <div class="plan-name">Al A Carte</div>
    <div class="plan-sub">As Needed Basis</div>
    <svg width="52" height="52" viewBox="0 0 52 52"><circle cx="26" cy="26" r="26" fill="#fff" fill-opacity=".22"/><path d="M20 16l14 10-14 10z" fill="#fff" fill-opacity=".45"/></svg>
  </div>
  <div class="notch"></div>

  <div class="from">STARTS @ FROM</div>
  <div class="price"><sup>$</sup>37.00</div>
  <div class="price-unit">Video Format</div>
  <div class="rule-s" style="top:150px"></div>
  <div class="acc" style="top:164px">INCLUDED FEATURES
    <svg width="8" height="8" viewBox="0 0 8 8"><path d="M2 3l2 2 2-2" fill="none" stroke="#333" stroke-width="1.1"/></svg></div>
  <div class="rule-s" style="top:188px"></div>

  <ul class="features">
    <li><svg width="9" height="6" viewBox="0 0 9 6"><path d="M.5 3l2 2L6 1M3.5 3.5L5 5l3.5-4" fill="none" stroke="#999" stroke-width=".8"/></svg>Fully Custom Video Ads</li>
    <li><svg width="9" height="6" viewBox="0 0 9 6"><path d="M.5 3l2 2L6 1M3.5 3.5L5 5l3.5-4" fill="none" stroke="#999" stroke-width=".8"/></svg>As Fast As 24 Hour Turn Around</li>
    <li><svg width="9" height="6" viewBox="0 0 9 6"><path d="M.5 3l2 2L6 1M3.5 3.5L5 5l3.5-4" fill="none" stroke="#999" stroke-width=".8"/></svg>Unlimited Revisions</li>
    <li><svg width="9" height="6" viewBox="0 0 9 6"><path d="M.5 3l2 2L6 1M3.5 3.5L5 5l3.5-4" fill="none" stroke="#999" stroke-width=".8"/></svg>Convert Any Static Ad To Video Ad</li>
    <li><svg width="9" height="6" viewBox="0 0 9 6"><path d="M.5 3l2 2L6 1M3.5 3.5L5 5l3.5-4" fill="none" stroke="#999" stroke-width=".8"/></svg>Four Essential Video Formats</li>
    <li><svg width="9" height="6" viewBox="0 0 9 6"><path d="M.5 3l2 2L6 1M3.5 3.5L5 5l3.5-4" fill="none" stroke="#999" stroke-width=".8"/></svg>Wide Video Format</li>
    <li><svg width="9" height="6" viewBox="0 0 9 6"><path d="M.5 3l2 2L6 1M3.5 3.5L5 5l3.5-4" fill="none" stroke="#999" stroke-width=".8"/></svg>Large Square Video Format</li>
    <li><svg width="9" height="6" viewBox="0 0 9 6"><path d="M.5 3l2 2L6 1M3.5 3.5L5 5l3.5-4" fill="none" stroke="#999" stroke-width=".8"/></svg>Vertical Video Format</li>
    <li><svg width="9" height="6" viewBox="0 0 9 6"><path d="M.5 3l2 2L6 1M3.5 3.5L5 5l3.5-4" fill="none" stroke="#999" stroke-width=".8"/></svg>Pixora Cover Video Format</li>
    <li><svg width="9" height="6" viewBox="0 0 9 6"><path d="M.5 3l2 2L6 1M3.5 3.5L5 5l3.5-4" fill="none" stroke="#999" stroke-width=".8"/></svg>Content Done For You</li>
  </ul>
  <div class="fscroll"></div>

  <div class="rule-s" style="top:407.5px"></div>
  <div class="acc" style="top:421px">ORDER SUMMARY
    <svg width="8" height="8" viewBox="0 0 8 8"><path d="M2 3l2 2 2-2" fill="none" stroke="#333" stroke-width="1.1"/></svg></div>
  <div class="rule-s" style="top:445.5px"></div>

  <div class="qty-label">How many video Ads:</div>
  <div class="stepper"><span class="pm">−</span><span class="num">01</span><span class="pm">+</span></div>

  <div class="sum-row sum-big" style="top:512px"><span class="k" style="right:110px">Total:</span><span class="v">$37.00</span></div>
  <div class="sum-row" style="top:545px"><span class="k">Qty Discount:</span><span class="v">$19.80</span></div>
  <div class="sum-row" style="top:560px"><span class="k">Price Per Video Format:</span><span class="v">$00.20</span></div>
  <div class="sum-row promo" style="top:575px"><span class="k">Promo Code Discount:</span><span class="v">$00.20</span></div>
  <div class="sum-row sum-big" style="top:602px"><span class="k">Grand Total:</span><span class="v red">$79.20</span></div>
</aside>

<footer class="footer">
  <div class="f-brand"><i></i>VIMLO</div>
  <div class="f-tag">MARKETING VIDEOS MADE FOR YOU</div>
  <div class="f-claim">CREATED BY A MARKETER FOR MARKETERS.</div>

  <h4 class="f-head" style="left:550px">Quick Links</h4>
  <div class="f-bar" style="left:550px"></div>
  <ul class="f-links">
    <li>How It Works</li><li>Term Of Service</li><li>Privacy Policy</li><li>Cookies Policy</li>
  </ul>

  <h4 class="f-head" style="left:728px">About Us</h4>
  <div class="f-bar" style="left:728px"></div>
  <p class="f-about">With Vimlo, you simply let us know what you want to promote and we will have your video ad finished as soon as 24 hours!</p>
  <div class="socials"><span></span><span></span><span></span><span></span><span></span></div>
</footer>

</body>
</html>
```